Business Card Design

We are a manufacturing and distribution company with most of our customer base being supermarkets. We have established brand guidelines that are attached.

```html
<!DOCTYPE html>
<html lang="en">
<head>
<meta charset="utf-8">
<title>Norvale Business Card</title>
<link rel="stylesheet" href="https://fonts.googleapis.com/css2?family=Archivo:wdth,wght@62..125,400..800&display=swap">
<style>
  :root {
    --page-bg: #e9e9e7;
    --card-bg: #252324;
    --edge-red: #d81f26;
    --accent-red: #e0262d;
    --text-white: #f4f4f4;
    --text-soft: #e2e2e2;
    --rule: #cfcfcf;
  }
  * { box-sizing: border-box; margin: 0; padding: 0; }
  html, body {
    width: 1200px; height: 802px; overflow: hidden;
    background: var(--page-bg);
    font-family: "Archivo", Arial, sans-serif;
  }
  .stage {
    position: relative; width: 1200px; height: 802px;
    display: flex; align-items: center; justify-content: center; gap: 60px;
  }
  .card {
    position: relative; width: 525px; height: 300px;
    background: var(--card-bg);
    border: 3px solid var(--edge-red);
    overflow: hidden;
  }
  /* Front */
  .brand {
    position: absolute; top: 58px; right: 48px;
    display: flex; align-items: center; gap: 12px;
  }
  .brand-square { width: 18px; height: 18px; background: var(--accent-red); }
  .brand-name {
    color: var(--text-white); font-weight: 800; font-stretch: 125%;
    font-size: 30px; letter-spacing: 1px;
  }
  .divider {
    position: absolute; left: 48px; right: 48px; top: 176px;
    height: 1px; background: var(--rule);
  }
  .person { position: absolute; left: 48px; bottom: 134px; }
  .person-name {
    color: var(--accent-red); font-weight: 600; font-size: 17px;
    letter-spacing: .5px; text-transform: uppercase;
  }
  .person-role { color: var(--text-soft); font-size: 14px; margin-top: 2px; }
  .contacts {
    position: absolute; left: 48px; top: 190px;
    list-style: none; display: flex; flex-direction: column; gap: 3px;
  }
  .contacts li {
    display: flex; align-items: center; gap: 8px;
    color: var(--text-soft); font-size: 15px;
  }
  .contacts svg { width: 12px; height: 12px; flex: none; }
  .address {
    position: absolute; right: 48px; top: 190px; text-align: right;
    color: var(--text-soft); font-size: 14px; line-height: 1.3;
  }
  /* Back */
  .back-name {
    position: absolute; right: 40px; top: 112px;
    color: var(--text-white); font-weight: 800; font-stretch: 125%;
    font-size: 50px; letter-spacing: 2px;
  }
</style>
</head>
<body>
<main class="stage">
  <section class="card card-front">
    <div class="brand">
      <span class="brand-square"></span>
      <span class="brand-name">NORVALE</span>
    </div>
    <div class="person">
      <p class="person-name">Daniel Reyes</p>
      <p class="person-role">Manager</p>
    </div>
    <div class="divider"></div>
    <ul class="contacts">
      <li>
        <svg viewBox="0 0 12 12" fill="none" stroke="#e0262d" stroke-width="1.6"><path d="M2.5 1.5c-1.5 1.5 0 4.5 2 6.5s5 3.5 6.5 2l-2-2-1.5 1c-1-.5-2.5-2-3-3l1-1.5z"/></svg>
        555-014-2100
      </li>
      <li>
        <svg viewBox="0 0 12 12" fill="none" stroke="#e0262d" stroke-width="1.3"><rect x="1" y="2.5" width="10" height="7"/><path d="M1 2.5l5 4 5-4"/></svg>
        hello@norvale.com
      </li>
      <li>
        <svg viewBox="0 0 12 12" fill="none" stroke="#e0262d" stroke-width="1.2"><circle cx="6" cy="6" r="5"/><ellipse cx="6" cy="6" rx="2.2" ry="5"/><path d="M1 6h10M2 3.5h8M2 8.5h8"/></svg>
        www.norvale.com
      </li>
    </ul>
    <p class="address">Your address, city<br>state, ZIP 0000</p>
  </section>

  <section class="card card-back">
    <p class="back-name">NORVALE</p>
  </section>
</main>
</body>
</html>
```